Sunscreen Package Design Modern SPF 50

Update current package design to a more modern design target women 16-40 Do not make it playful. Solana Mesa is home to movie stars and high income business people PalmSprings is one of the most desired vacation areas in the world. The sun shines 350 days a year. World class Tennis and Golf tournaments are held every year with the worlds top players attending these tournaments

Target Market(s)

Women

Industry/Entity Type

Skin Protection

Font styles to use
Sans Serif

Requirements
Must have
• The words Solana Mesa and VELORIMA

```html
<!DOCTYPE html>
<html lang="en">
<head>
<meta charset="utf-8">
<title>Solana Mesa VELORIMA Sunscreen SPF 50</title>
<link href="https://fonts.googleapis.com/css2?family=Montserrat:wght@400;500;600;700&display=swap" rel="stylesheet">
<style>
:root{
  --bg:#f4f1ed;
  --peach-top:#fde6cf;
  --peach-bottom:#f9d3ad;
  --orange:#e9561a;
  --orange-deep:#d9470f;
  --gold:#c9902f;
  --gold-light:#e8b860;
  --ink:#1d1410;
  --brown:#6b3a12;
  --white:#fffaf4;
  --line:#5a4030;
}
*{box-sizing:border-box;margin:0;padding:0}
html,body{width:865px;height:1200px;overflow:hidden;background:var(--bg)}
body{font-family:"Montserrat",sans-serif;color:var(--ink);position:relative}
.panel{position:absolute;top:40px;width:380px;height:1120px;border-radius:16px;overflow:hidden;
  background:linear-gradient(180deg,var(--peach-top),var(--peach-bottom));
  box-shadow:0 6px 20px rgba(120,70,30,.15)}
.panel--front{left:24px}
.panel--back{left:461px}
.center{position:absolute;left:0;right:0;text-align:center}

/* front */
.brand-mark{position:absolute;left:128px;top:118px;width:124px;height:124px;border-radius:50%;
  background:var(--orange)}
.brand-name{font-weight:500;color:var(--ink);line-height:1}
.front-brand{top:292px;font-size:40px;letter-spacing:1px}
.front-name{top:362px;font-size:28px;letter-spacing:9px;font-weight:500}
.rule{position:absolute;height:1.5px;background:var(--gold)}
.front-rule{left:65px;width:250px;top:410px}
.front-product{top:424px;font-size:27px;letter-spacing:5px;font-weight:500}
.wave{position:absolute;left:0;top:0}
.spf-badge{position:absolute;left:103px;top:508px;width:174px;height:174px;border-radius:50%;
  background:radial-gradient(circle,#fff 60%,#fbeee0);border:5px solid var(--gold);
  text-align:center;color:var(--brown)}
.spf-badge .spf{display:block;margin-top:20px;font-size:22px;font-weight:600;letter-spacing:2px}
.spf-badge .num{display:block;font-size:62px;font-weight:700;line-height:.95;letter-spacing:-2px}
.spf-badge .bs{display:block;font-size:15px;font-weight:600;letter-spacing:2px;line-height:1.2;color:var(--ink)}
.claim{color:var(--white);font-size:17px;letter-spacing:1.5px;font-weight:500}
.claim-small{color:var(--white);font-size:13px;letter-spacing:1px}
.white-rule{position:absolute;height:1px;background:rgba(255,240,220,.8)}

/* back */
.back-brand{top:112px;font-size:30px;letter-spacing:1px}
.back-name{top:160px;font-size:20px;letter-spacing:7px;font-weight:500}
.sunburst{position:absolute;right:-40px;top:110px;width:170px;height:250px;
  background:radial-gradient(ellipse at 100% 40%,rgba(233,86,26,.55),rgba(233,86,26,0) 70%)}
.tagline{top:226px;font-size:17px;line-height:1.3;padding:0 30px}
.intro{top:285px;font-size:12.3px;line-height:1.45;padding:0 22px}
.features{position:absolute;top:370px;left:16px;right:16px;display:flex;justify-content:space-around}
.feature{width:76px;text-align:center;font-size:11.5px;line-height:1.3}
.feature svg{display:block;margin:0 auto 6px}
.drug-facts{position:absolute;left:48px;top:486px;width:286px;border:1.3px solid var(--line);border-radius:6px;font-size:8.3px;line-height:1.38;padding:0 8px}
.drug-facts h2{font-size:14px;font-weight:600;padding:4px 0 3px;border-bottom:1px solid var(--line)}
.df-section{padding:4px 2px;border-bottom:1px solid var(--line)}
.df-section:last-child{border-bottom:none}
.df-section strong{font-weight:700;font-size:9.2px}
.df-row{display:flex}
.df-row .active{flex:1;padding-right:6px;border-right:1px solid var(--line)}
.df-row .purpose{width:70px;padding-left:8px}
.badges{top:802px;font-size:11.3px;line-height:1.6}
.badges span.sep{display:inline-block;width:1px;height:12px;background:var(--gold);margin:0 10px;vertical-align:-2px}
.contact{top:849px;font-size:9.5px;line-height:1.7}
.contact strong{font-weight:700}
.net{position:absolute;left:22px;top:912px;font-size:12px}
</style>
</head>
<body>

<section class="panel panel--front" aria-label="Front label">
  <div class="brand-mark" aria-hidden="true"></div>
  <h1 class="center brand-name front-brand">SOLANA MESA</h1>
  <p class="center front-name">VELORIMA</p>
  <div class="rule front-rule"></div>
  <p class="center front-product">SUNSCREEN</p>

  <svg class="wave" width="380" height="1120" viewBox="0 0 380 1120" aria-hidden="true">
    <defs>
      <linearGradient id="orangeFill" x1="0" y1="0" x2="0" y2="1">
        <stop offset="0" stop-color="#ef6a25"/>
        <stop offset="1" stop-color="#e04e14"/>
      </linearGradient>
    </defs>
    <path d="M0,700 C110,630 230,600 300,540 C340,505 365,470 380,430 L380,1120 L0,1120 Z" fill="url(#orangeFill)"/>
    <path d="M0,690 C110,620 230,590 300,530 C340,495 365,460 380,420" fill="none" stroke="#d9a04a" stroke-width="7"/>
  </svg>

  <div class="spf-badge">
    <span class="spf">SPF</span>
    <span class="num">50</span>
    <span class="bs">BROAD<br>SPECTRUM</span>
  </div>

  <p class="center claim" style="top:722px">UVA+UVB PROTECTION</p>
  <div class="white-rule" style="left:95px;width:190px;top:759px"></div>
  <p class="center claim" style="top:777px">WATER RESISTANT</p>
  <p class="center claim" style="top:799px;font-size:14px">(80 MINUTES)</p>
  <div class="white-rule" style="left:140px;width:100px;top:832px"></div>
  <p class="center claim" style="top:848px">HYDRATES &amp; NOURISHES</p>
  <p class="center claim-small" style="top:876px">ALOE &nbsp;•&nbsp; ANTIOXIDANTS &nbsp;•&nbsp; VITAMIN E</p>
  <p class="center claim" style="top:932px;font-size:19px;letter-spacing:.5px">3 FL OZ / 88 mL</p>
</section>

<section class="panel panel--back" aria-label="Back label">
  <div class="sunburst" role="img" aria-label="Soft orange sun-ray decoration"></div>
  <h2 class="center brand-name back-brand">SOLANA MESA</h2>
  <p class="center back-name">VELORIMA</p>

  <p class="center tagline">Luxury sun protection for<br>a life lived under the sun.</p>
  <p class="center intro">Solana Mesa VELORIMA delivers advanced broad spectrum protection with a hydrating, lightweight, non-greasy formula — so you can enjoy every sunny moment with confidence.</p>

  <div class="features">
    <div class="feature">
      <svg width="46" height="46" viewBox="0 0 46 46" aria-hidden="true"><circle cx="23" cy="23" r="21" fill="none" stroke="#e9561a" stroke-width="1.5"/><path d="M15,31 C15,20 22,14 31,14 C31,24 25,31 15,31 Z M15,31 L26,20" fill="none" stroke="#e9561a" stroke-width="1.5"/></svg>
      Hydrates<br>Skin
    </div>
    <div class="feature">
      <svg width="46" height="46" viewBox="0 0 46 46" aria-hidden="true"><circle cx="23" cy="23" r="21" fill="none" stroke="#e9561a" stroke-width="1.5"/><path d="M23,12 L25,21 L34,23 L25,25 L23,34 L21,25 L12,23 L21,21 Z" fill="none" stroke="#e9561a" stroke-width="1.5"/></svg>
      Non-Greasy<br>Finish
    </div>
    <div class="feature">
      <svg width="46" height="46" viewBox="0 0 46 46" aria-hidden="true"><circle cx="23" cy="23" r="21" fill="none" stroke="#e9561a" stroke-width="1.5"/><path d="M23,12 L32,15 L32,23 C32,29 28,32 23,35 C18,32 14,29 14,23 L14,15 Z" fill="#e9561a"/></svg>
      Antioxidant<br>Rich
    </div>
    <div class="feature">
      <svg width="46" height="46" viewBox="0 0 46 46" aria-hidden="true"><circle cx="23" cy="23" r="21" fill="none" stroke="#e9561a" stroke-width="1.5"/><path d="M23,33 L23,16 M23,26 L17,20 L17,14 M23,24 L29,18 L29,13 M14,33 L32,33" fill="none" stroke="#e9561a" stroke-width="1.6" stroke-linecap="round"/></svg>
      Reef<br>Friendly
    </div>
  </div>

  <div class="drug-facts">
    <h2>Drug Facts</h2>
    <div class="df-section df-row">
      <div class="active"><strong>Active Ingredients:</strong><br>Avobenzone 3.0%, Homosalate 10.0%, Octisalate 5.0%, Octocrylene 7.0%</div>
      <div class="purpose"><strong>Purpose:</strong><br>Sunscreen</div>
    </div>
    <div class="df-section"><strong>Uses:</strong><br>• Helps prevent sunburn, if used as directed with other sun protection measures.</div>
    <div class="df-section"><strong>Warnings:</strong><br>For external use only. Do not use on damaged or broken skin. When using this product keep out of eyes. Rinse with water to remove. Stop use and ask a doctor if rash occurs. Keep out of reach of children. If swallowed, get medical help or contact a Poison Control Center right away.</div>
    <div class="df-section"><strong>Directions:</strong><br>• Apply generously 15 minutes before sun exposure.<br>• Reapply at least every 2 hours.<br>• Use a water resistant sunscreen if swimming or sweating.</div>
  </div>

  <p class="center badges">Dermatologist Recommended<span class="sep"></span>Reef Friendly<br>Paraben Free<span class="sep"></span>Cruelty Free</p>
  <p class="center contact"><strong>Full Ingredients:</strong> See carton or visit our website.<br><strong>Questions?</strong> questions@velorima.com</p>
  <p class="net">3 FL OZ / 88 mL</p>
</section>

</body>
</html>
```